Book Cover on Entrepreneurship for Eye Doctors

Book Title: The Lens Clinic Founder: How to launch your practice with flair
Author: Morvan Tessaleq, Optom, MBA, DBA, EIC
I need a Book Cover with the following descriptions:
Topic: the book topic is entrepreneurship knowledge for eye care professionals.
The book's audience: eye care professionals who you know as Opticians, who sell eyeglasses and sunglasses;
Optometrists, test eyes, fit contact lenses, and prescribe medication
Ophthalmologists, perform eye surgery
More about the audience:
1- Young eye care professionals who don’t know about entrepreneurship and those who are stuck in the 9-to-5 job;
2- This is the first book written on entrepreneurship with eye care professionals in mind.
3- Private practice owners the established business guys who are looking to grow their business;
4- Many eye care professionals are MBA holders they may have learned a little bit about entrepreneurship during their MBA studies.
Use the sample cover above and the suggestions that follow as a guide:
1- The cover should be very simple leaving an empty space somewhere to sign the book;
2- The Title and author name should use a modern font;
3- The cover should provide info about what's inside the book through illustrations, for example:
a- Gears: illustrating entrepreneur growth mindset (or anything more explicit)
b- Spectacles, sunglasses, lenses, eye drops, or any other eye care-related correction tools illustrating eye care (or anything more explicit)
c- Symbols illustrating ideas, opportunity, and profit, like money, charts, light bulbs, brain, and coins,...(or anything more explicit)
d- Entrepreneurship illustrated by Briefcase, tie, suit,... (or anything more explicit)

The rest is your creativity and imagination interplay.

Target Market(s)

Eye care professionals: Opticians, Optometrists, Ophthalmologists, Eye Care Administrators, Students in eye specialties.

Industry/Entity Type

eye care

Requirements
Must have
• 1- The cover should be very simple leaving an empty space somewhere to sign the book; 2- The Title and author name should use a modern font; 3- The cover should provide info about what's inside the book through illustrations, for example: a- Gears: illustrating entrepreneur growth mindset (or anything more explicit) b- Spectacles, sunglasses, lenses, eye drops, or any other eye care-related correction tools illustrating eye care (or anything more explicit) c- Symbols illustrating ideas, opportunity, and profit, like money, charts, light bulbs, brain, and coins,...(or anything more explicit) d- Entrepreneurship illustrated by Briefcase, tie, suit,... (or anything more explicit)

```html
<!DOCTYPE html>
<html lang="en">
<head>
<meta charset="utf-8">
<title>The Lens Clinic Founder — Book Cover</title>
<link href="https://fonts.googleapis.com/css2?family=Open+Sans:wght@400;600;700;800&display=swap" rel="stylesheet">
<style>
  :root {
    --backdrop: #8c8c8c;
    --cover-top: #ffffff;
    --cover-bottom: #e4e4e4;
    --ink: #141414;
    --ink-soft: #2b2b2b;
    --accent-red: #8a1a0c;
    --bag-dark: #1c1a19;
    --bag-mid: #3a3431;
  }
  html, body {
    margin: 0;
    padding: 0;
    width: 1200px;
    height: 1200px;
    overflow: hidden;
    background: var(--backdrop);
  }
  .cover {
    position: absolute;
    left: 239px;
    top: 60px;
    width: 722px;
    height: 1080px;
    background: linear-gradient(180deg, var(--cover-top) 0%, var(--cover-top) 45%, var(--cover-bottom) 100%);
    font-family: "Open Sans", Arial, sans-serif;
    color: var(--ink);
    text-align: center;
  }
  .title {
    position: absolute;
    top: 104px;
    left: 0;
    width: 100%;
    margin: 0;
    font-weight: 400;
  }
  .title span { display: block; line-height: 1; }
  .title-lead {
    font-size: 66px;
    font-weight: 400;
    letter-spacing: 1px;
  }
  .title-main {
    margin-top: 18px;
    font-size: 68px;
    font-weight: 800;
    letter-spacing: -0.5px;
  }
  .title-accent {
    margin-top: 18px;
    font-size: 70px;
    font-weight: 600;
    color: var(--accent-red);
    letter-spacing: 0.5px;
  }
  .subtitle {
    position: absolute;
    top: 362px;
    left: 0;
    width: 100%;
    margin: 0;
    font-size: 23px;
    font-weight: 600;
    letter-spacing: 0.8px;
    color: var(--ink-soft);
  }
  .cover-photo {
    position: absolute;
    left: 177px;
    top: 510px;
    width: 388px;
    height: 326px;
    border-radius: 10px 10px 6px 6px;
    background: radial-gradient(ellipse at 45% 40%, var(--bag-mid) 0%, var(--bag-dark) 70%);
  }
  .author {
    position: absolute;
    top: 955px;
    left: 0;
    width: 100%;
  }
  .author-name {
    margin: 0;
    font-size: 38px;
    font-weight: 800;
    letter-spacing: 3px;
    line-height: 1.05;
  }
  .author-credentials {
    margin: 4px 0 0;
    font-size: 27px;
    font-weight: 700;
    letter-spacing: 2.5px;
    color: var(--ink-soft);
  }
</style>
</head>
<body>
  <main class="cover">
    <h1 class="title">
      <span class="title-lead">THE</span>
      <span class="title-main">LENS CLINIC</span>
      <span class="title-accent">FOUNDER</span>
    </h1>
    <p class="subtitle">HOW TO LAUNCH YOUR PRACTICE WITH FLAIR</p>
    <div class="cover-photo" role="img" aria-label="Photo of a black leather briefcase with a stethoscope draped over its handle"></div>
    <footer class="author">
      <p class="author-name">MORVAN TESSALEQ</p>
      <p class="author-credentials">OPTOM, MBA, DBA, EIC</p>
    </footer>
  </main>
</body>
</html>
```